Power Pilot with goSwap messages

Power Pilot is an energy switching platform, which automatically switches you to the best energy tariff. All messages are attached.

Target Market(s)

austria

Number of Pages Required

4 page

```html
<!DOCTYPE html>
<html lang="de">
<head>
<meta charset="utf-8">
<title>Power Pilot – Spaß am Wechseln</title>
<link rel="stylesheet" href="https://fonts.googleapis.com/css2?family=Open+Sans:wght@300;400;600;700&family=Lato:wght@300;400;700&display=swap">
<style>
:root{
  --orange:#f4a21b;
  --teal:#17a096;
  --teal-dark:#00664f;
  --slate:#3d474c;
  --ink:#3a3a3a;
  --muted:#666;
  --light:#f4f4f4;
  --white:#fff;
}
*{box-sizing:border-box;margin:0;padding:0}
html,body{width:760px;height:1200px;overflow:hidden;background:var(--white)}
body{position:relative;font-family:"Open Sans",Arial,sans-serif;color:var(--ink)}
.abs{position:absolute}

/* hero */
.hero-visual{left:0;top:0;width:450px;height:380px;background:radial-gradient(circle at 62% 22%,#e9f7a0 0,#9fcf3c 14%,#4f8f1e 45%,#2e5c12 100%)}
.brand{left:30px;top:8px;font-family:"Open Sans",sans-serif;font-weight:700;font-size:17px;color:var(--orange);display:flex;align-items:center;gap:6px}
.brand .dot{width:12px;height:12px;border-radius:50%;background:var(--orange)}
.menu-toggle{left:414px;top:20px;width:16px}
.menu-toggle span{display:block;height:2px;background:rgba(255,255,255,.5);margin-bottom:3px}
.hero-title{left:22px;top:141px;font-weight:700;font-size:19px;color:var(--white);letter-spacing:.3px;white-space:nowrap}
.hero-lead{left:21px;top:179px;font-size:12px;line-height:14px;color:var(--white)}
.btn-read{left:28px;top:248px;width:111px;height:25px;background:var(--orange);color:#3b2a05;font-size:8.5px;display:flex;align-items:center;justify-content:center}

/* promise card */
.promise-panel{left:450px;top:0;width:310px;height:345px;background:var(--light)}
.promise-card{left:487px;top:37px;width:236px;height:235px;border:6px solid #b5b5b5;background:#f6f6f6;box-shadow:2px 3px 4px rgba(0,0,0,.25)}
.promise-title{left:20px;top:24px;font-weight:700;font-size:14px;line-height:39px;letter-spacing:.4px;color:#333}
.promise-text{left:22px;top:141px;width:190px;font-size:8px;line-height:12.5px;color:var(--muted)}
.promise-tag{left:22px;top:187px;font-size:17px;color:#444}
.power-badge{left:149px;top:4px;width:56px;height:56px}

/* who we are */
.who{left:0;top:380px;width:530px;height:180px;background:linear-gradient(135deg,#1fb0a4,#0f9187 60%,#16a79b)}
.who h2{position:absolute;left:18px;top:46px;font-size:15px;font-weight:700;color:var(--white)}
.who p{position:absolute;left:18px;top:78px;width:345px;font-size:7.4px;line-height:12px;color:var(--white)}
.who svg{position:absolute;left:17px;top:128px}
.savings-photo{left:388px;top:310px;width:355px;height:227px;background:linear-gradient(120deg,#2d4f86 0%,#3a5f95 40%,#cfd3d6 75%,#eef0f0 100%);box-shadow:2px 3px 5px rgba(0,0,0,.35)}

/* services */
.service{top:560px;width:253px;height:248px;text-align:center}
.service.alt{background:var(--light)}
.service svg{position:absolute;left:50%;top:48px;transform:translateX(-50%)}
.service h3{position:absolute;left:0;right:0;top:116px;font-weight:400;font-size:15px;line-height:16px;color:#444;text-transform:uppercase}
.service .rule{position:absolute;left:110px;width:33px;height:1px;background:var(--orange)}
.service p{position:absolute;left:38px;right:38px;font-size:7.8px;line-height:13px;color:#555}

/* stats */
.stats{left:0;top:808px;width:760px;height:107px;display:flex}
.stat{flex:1;border-right:1px solid rgba(255,255,255,.35);text-align:center;color:var(--white);position:relative}
.stat svg{position:absolute;left:50%;top:22px;transform:translateX(-50%)}
.stat .val{position:absolute;left:0;right:0;top:36px;font-size:10px;font-weight:600}
.stat .val small{font-size:6px}
.stat .label{position:absolute;left:4px;right:4px;top:68px;font-size:7.5px;line-height:11px}

/* steps */
.steps{left:0;top:915px;width:760px;height:202px;background:var(--slate);color:var(--white);text-align:center}
.steps h2{position:absolute;left:0;right:0;top:18px;font-weight:300;font-size:25px;line-height:31px}
.steps p{position:absolute;left:0;right:0;top:88px;font-weight:300;font-size:15.5px;color:#e8e8e8}
.steps .power-btn{position:absolute;left:240px;top:113px}
.btn-step{position:absolute;left:335px;top:135px;width:90px;height:27px;border:1px solid var(--orange);color:var(--orange);font-size:8.5px;font-weight:600;display:flex;align-items:center;justify-content:center}

/* footer */
.contact-bar{left:0;top:1117px;width:760px;height:41px;background:#f3f3f3;font-size:7px;color:#444;display:flex;align-items:center;padding-left:17px}
.contact-bar .item{display:flex;align-items:center;gap:4px;padding-right:9px;margin-right:9px;border-right:1px solid #ccc}
.contact-bar .item:last-of-type{border-right:none}
.contact-bar svg{fill:var(--teal-dark)}
.follow{position:absolute;right:17px;top:15px;display:flex;gap:7px;align-items:center}
.follow span.ic{width:6px;height:6px;border-radius:50%;background:#555}
.footer{left:0;top:1158px;width:760px;height:42px;background:var(--white);border-bottom:4px solid var(--teal-dark)}
.footer .brand{left:17px;top:0;font-size:17px}
.copyright{position:absolute;right:44px;top:16px;font-size:6.8px;color:#444}
.to-top{position:absolute;left:726px;top:12px;width:16px;height:16px;border-radius:50%;background:var(--teal-dark)}
</style>
</head>
<body>

<div class="abs hero-visual" role="img" aria-label="Glowing light bulbs lying on fresh green grass"></div>
<div class="abs brand">Power Pilot <span class="dot"></span></div>
<div class="abs menu-toggle"><span></span><span></span><span></span></div>
<h1 class="abs hero-title">SPAß AM WECHSELN – POWER PILOT</h1>
<p class="abs hero-lead">Energieversorger wechseln<br>ist langweilig.<br>Dann streichen wir es<br>doch von Deiner</p>
<div class="abs btn-read">Read More About Us &nbsp;»</div>

<div class="abs promise-panel"></div>
<div class="abs promise-card">
  <svg class="abs power-badge" viewBox="0 0 56 56">
    <circle cx="28" cy="28" r="26" fill="#fff"/>
    <circle cx="28" cy="28" r="22" fill="none" stroke="#333" stroke-width="3.5"/>
    <path d="M21 21a10 10 0 1 0 14 0" fill="none" stroke="#333" stroke-width="3" stroke-linecap="round"/>
    <line x1="28" y1="16" x2="28" y2="28" stroke="#333" stroke-width="3" stroke-linecap="round"/>
  </svg>
  <h2 class="abs promise-title">GÜNSTIGE<br>ENERGIERECHNUNGEN<br>FÜR IMMER.</h2>
  <p class="abs promise-text">We are brand storytellers - creating powerful and long-term connections between brands and their custome.</p>
  <p class="abs promise-tag">Think Really Simple :)</p>
</div>

<section class="abs who">
  <h2>WHO WE ARE</h2>
  <p>We create campaigns, communications strategies and marketing programmes that are impossible to ignore – blending cutting-edge technology, traditional media and a whole lot more, to create relevant, insight driven, strategic work that cuts-through and stands out.</p>
  <svg width="16" height="10" viewBox="0 0 16 10"><path d="M0 5h14M10 1l4 4-4 4" fill="none" stroke="#fff" stroke-width="1.6"/></svg>
</section>
<div class="abs savings-photo" role="img" aria-label="Hand dropping a coin into a glass jar of savings next to a calculator"></div>

<section class="abs service" style="left:0">
  <svg width="54" height="52" viewBox="0 0 54 52" fill="none" stroke="#666" stroke-width="2">
    <rect x="4" y="4" width="32" height="44"/><path d="M12 16l14 4-12 6 14 6" stroke="#f4a21b"/>
    <path d="M42 6h6v36l-3 6-3-6z"/>
  </svg>
  <h3>Wir führen die Suche durch</h3>
  <span class="rule" style="top:146px"></span>
  <p style="top:156px">Lorem ipsum dolor sit amet, consectetur adipiscing elit. Aenean vitae purus imperdiet, euismod ante eu, pulvinar eros. Vivamus et commodo quam, sed facili-sis felis praesent nunc.</p>
</section>
<section class="abs service alt" style="left:253px;width:254px">
  <svg width="54" height="52" viewBox="0 0 54 52" fill="none" stroke="#666" stroke-width="2">
    <rect x="3" y="4" width="48" height="34"/><path d="M22 38v8h10v-8M16 47h22"/>
    <path d="M27 8c5 4 6 12 4 20h-8c-2-8-1-16 4-20z" stroke="#f4a21b"/><path d="M23 24l-4 6h5M31 24l4 6h-5" stroke="#f4a21b"/>
  </svg>
  <h3>Wir wechseln dich</h3>
  <span class="rule" style="top:146px"></span>
  <p style="top:156px">Lorem ipsum dolor sit amet, consectetur adipiscing elit. Aenean vitae purus imperdiet, euismod ante eu, pulvinar eros. Vivamus et commodo quam, sed facili-sis felis praesent nunc.</p>
</section>
<section class="abs service" style="left:507px">
  <svg width="54" height="52" viewBox="0 0 54 52" fill="none" stroke="#666" stroke-width="2">
    <circle cx="27" cy="26" r="9" stroke="#f4a21b" stroke-width="3"/>
    <circle cx="8" cy="8" r="4"/><circle cx="46" cy="8" r="4"/><circle cx="8" cy="44" r="4"/><circle cx="46" cy="44" r="4"/><circle cx="27" cy="4" r="3"/>
    <path d="M11 11l9 8M43 11l-9 8M11 41l9-8M43 41l-9-8M27 7v10"/>
  </svg>
  <h3>Wir wechseln dich<br>immer wieder</h3>
  <span class="rule" style="top:146px"></span>
  <p style="top:165px">Lorem ipsum dolor sit amet, consectetur adipiscing elit. Aenean vitae purus imperdiet, euismod ante eu, pulvinar eros. Vivamus et commodo quam, sed facili-sis felis praesent nunc.</p>
</section>

<section class="abs stats">
  <div class="stat" style="background:#f5a21b"><svg width="42" height="42" viewBox="0 0 42 42"><circle cx="21" cy="21" r="18" fill="none" stroke="rgba(255,255,255,.35)" stroke-width="4"/><circle cx="21" cy="21" r="18" fill="none" stroke="#fff" stroke-width="4" pathLength="100" stroke-dasharray="95 100" transform="rotate(-90 21 21)"/></svg><div class="val">95<small>%</small></div><div class="label">Brand Strategy</div></div>
  <div class="stat" style="background:#d59b21"><svg width="42" height="42" viewBox="0 0 42 42"><circle cx="21" cy="21" r="18" fill="none" stroke="rgba(255,255,255,.35)" stroke-width="4"/><circle cx="21" cy="21" r="18" fill="none" stroke="#fff" stroke-width="4" pathLength="100" stroke-dasharray="92 100" transform="rotate(-90 21 21)"/></svg><div class="val">92<small>%</small></div><div class="label">Creative</div></div>
  <div class="stat" style="background:#b1952b"><svg width="42" height="42" viewBox="0 0 42 42"><circle cx="21" cy="21" r="18" fill="none" stroke="rgba(255,255,255,.35)" stroke-width="4"/><circle cx="21" cy="21" r="18" fill="none" stroke="#fff" stroke-width="4" pathLength="100" stroke-dasharray="95 100" transform="rotate(-90 21 21)"/></svg><div class="val">95<small>%</small></div><div class="label">Digital Strategy</div></div>
  <div class="stat" style="background:#7d8a39"><svg width="42" height="42" viewBox="0 0 42 42"><circle cx="21" cy="21" r="18" fill="none" stroke="rgba(255,255,255,.35)" stroke-width="4"/><circle cx="21" cy="21" r="18" fill="none" stroke="#fff" stroke-width="4" pathLength="100" stroke-dasharray="87 100" transform="rotate(-90 21 21)"/></svg><div class="val">87<small>%</small></div><div class="label">Art Direction &amp;<br>Visual Design</div></div>
  <div class="stat" style="background:#557c41"><svg width="42" height="42" viewBox="0 0 42 42"><circle cx="21" cy="21" r="18" fill="none" stroke="rgba(255,255,255,.35)" stroke-width="4"/><circle cx="21" cy="21" r="18" fill="none" stroke="#fff" stroke-width="4" pathLength="100" stroke-dasharray="79 100" transform="rotate(-90 21 21)"/></svg><div class="val">79<small>%</small></div><div class="label">Campaign<br>Development</div></div>
  <div class="stat" style="background:#2f6f48"><svg width="42" height="42" viewBox="0 0 42 42"><circle cx="21" cy="21" r="18" fill="none" stroke="rgba(255,255,255,.35)" stroke-width="4"/><circle cx="21" cy="21" r="18" fill="none" stroke="#fff" stroke-width="4" pathLength="100" stroke-dasharray="82 100" transform="rotate(-90 21 21)"/></svg><div class="val">82<small>%</small></div><div class="label">Integrated<br>Production</div></div>
  <div class="stat" style="background:#00664f;border-right:none"><svg width="42" height="42" viewBox="0 0 42 42"><circle cx="21" cy="21" r="18" fill="none" stroke="rgba(255,255,255,.35)" stroke-width="4"/><circle cx="21" cy="21" r="18" fill="none" stroke="#fff" stroke-width="4" pathLength="100" stroke-dasharray="90 100" transform="rotate(-90 21 21)"/></svg><div class="val">90<small>%</small></div><div class="label">Media Services</div></div>
</section>

<section class="abs steps">
  <h2>Wir brauchen nicht viel von dir<br>1,2,3, ... 4.</h2>
  <p>Nie wieder über hohe Energiekosten ärgern. Power Pilot macht das schon.</p>
  <svg class="power-btn" width="70" height="70" viewBox="0 0 70 70">
    <circle cx="35" cy="35" r="34" fill="#2e3538"/>
    <circle cx="35" cy="35" r="29" fill="#444c50" stroke="#23292c" stroke-width="3"/>
    <path d="M28 27a11 11 0 1 0 14 0" fill="none" stroke="#1e2326" stroke-width="3.5" stroke-linecap="round"/>
    <line x1="35" y1="22" x2="35" y2="35" stroke="#1e2326" stroke-width="3.5" stroke-linecap="round"/>
  </svg>
  <div class="btn-step">Schritt 1 von 4</div>
</section>

<footer>
  <div class="abs contact-bar">
    <span class="item"><svg width="7" height="7" viewBox="0 0 10 10"><path d="M2 0l2 3-1 1c1 2 2 3 3 3l1-1 3 2-1 2C5 10 0 5 0 2z"/></svg>+00 (000) 000 0000</span>
    <span class="item"><svg width="8" height="6" viewBox="0 0 10 7"><path d="M0 0h10v7H0z M1 1l4 3 4-3" fill="none" stroke="#00664f"/></svg>info@domainname.com</span>
    <span class="item"><svg width="7" height="7" viewBox="0 0 10 10"><rect x="0" y="2" width="10" height="8"/></svg>+00 (000) 000 0000</span>
    <span class="item"><svg width="7" height="7" viewBox="0 0 10 10"><path d="M1 1h6v2H3v4h4V6h2v3H1z"/></svg>0678 Lorem ipsum dolor sit amet, Street, City, Country</span>
    <div class="follow">Follow Us: <span class="ic"></span><span class="ic"></span><span class="ic"></span></div>
  </div>
  <div class="abs footer">
    <div class="abs brand">Power Pilot <span class="dot"></span></div>
    <p class="copyright">© Copyright 2019 Power Pilot. All rights reserved.</p>
    <span class="to-top"></span>
  </div>
</footer>

</body>
</html>
```